Design a single page Shopify store web page

We are looking to have a page designed for a single page Shopify store with 2 products. We already have a basic structure that we like, though we are open to suggestions. We are looking for somebody to provide a design/color scheme that we can then implement using Shopify's templating system. We can handle the implementation(HTML / CSS / jS) as we already have 2 web developers on the team, but have not been able to find a design we liked.

The job would consist of providing a mockup (photoshop or otherwise) and any vector graphics you choose to create for the site (we can provide product photos and other images).

You can also look at http://brickwellgoods.com.au for some of our design direction we have used so far

Target Market(s)

Young Australian Males (18 - 49)

Industry/Entity Type

Store

Number of Pages Required

1 page

Font styles to use
Serif
Sans Serif

Requirements
Must have
• Single Page Design
• E-commerce Product Purchase
• Manly (whatever interpretation of that you have)

```html
<!DOCTYPE html>
<html lang="en">
<head>
<meta charset="utf-8">
<title>Brickwell — Automatate Your Life</title>
<link rel="stylesheet" href="https://fonts.googleapis.com/css2?family=Questrial&family=Open+Sans:wght@400;600&display=swap">
<style>
  :root {
    --ink: #141414;
    --footer: #1b1b1b;
    --blue: #10b0f0;
    --blue-deep: #0b93c9;
    --blue-text: #1ba8e8;
    --white: #ffffff;
    --paper: #ededed;
    --body-grey: #6a6a6a;
    --red: #e0302a;
    --logo-grey: #cfcfcf;
    --display: "Questrial", "Century Gothic", sans-serif;
    --body: "Open Sans", Arial, sans-serif;
  }
  * { box-sizing: border-box; margin: 0; padding: 0; }
  html, body { width: 1200px; height: 2308px; overflow: hidden; }
  body { position: relative; background: var(--white); font-family: var(--body); color: var(--ink); }

  /* Header */
  .site-header { position: absolute; left: 0; top: 0; width: 1200px; height: 114px; background: var(--ink); }
  .brand { position: absolute; left: 97px; top: 26px; display: flex; align-items: center; gap: 14px;
    font-family: var(--display); font-size: 30px; font-weight: 400; letter-spacing: 3px; color: var(--logo-grey); text-transform: uppercase; }
  .brand-dot { width: 34px; height: 34px; border-radius: 50%; background: var(--logo-grey); }
  .main-nav { position: absolute; top: 35px; left: 638px; height: 45px; display: flex; align-items: center; }
  .main-nav a { font-family: var(--body); font-size: 14px; color: var(--white); text-decoration: none; margin-right: 32px; }
  .main-nav a.signup { position: absolute; left: 316px; width: 146px; height: 45px; margin: 0; border-radius: 4px;
    background: var(--blue); display: flex; align-items: center; justify-content: center; }

  /* Hero */
  .hero { position: absolute; left: 0; top: 114px; width: 1200px; height: 494px; background: var(--blue); overflow: hidden; }
  .hero-photo { position: absolute; left: 0; top: 0; width: 1200px; height: 494px; }
  .hero-copy { position: absolute; right: 100px; top: 0; text-align: right; font-family: var(--display); color: var(--white); }
  .hero-title { position: absolute; right: 0; top: 120px; white-space: nowrap; font-size: 64px; font-weight: 400; }
  .hero-title .dark { color: var(--ink); }
  .hero-sub { position: absolute; right: 0; top: 209px; white-space: nowrap; font-size: 37px; line-height: 48px; font-weight: 400; }
  .hero-sub .dark { color: var(--ink); }
  .hero-when { position: absolute; right: 0; top: 320px; white-space: nowrap; font-size: 30px; }
  .slider-dots { position: absolute; left: 1040px; top: 387px; display: flex; gap: 7px; }
  .slider-dots span { width: 15px; height: 15px; border-radius: 50%; background: var(--white); border: 2px solid var(--ink); }
  .slider-dots span.active { background: var(--ink); }

  /* Section titles */
  .section-title { position: absolute; left: 0; width: 1200px; text-align: center; font-family: var(--display); font-size: 31px; font-weight: 400; }

  /* How it works */
  .how { position: absolute; left: 0; top: 608px; width: 1200px; height: 504px; background: var(--white); }
  .how .section-title { top: 30px; color: var(--ink); }
  .step { position: absolute; top: 112px; width: 300px; margin-left: -150px; text-align: center; }
  .step-icon { width: 198px; height: 198px; margin: 0 auto; border-radius: 50%; background: var(--blue);
    display: flex; align-items: center; justify-content: center; }
  .step h3 { margin-top: 15px; font-family: var(--display); font-weight: 400; font-size: 20px; }
  .step p { margin-top: 6px; font-size: 14.5px; line-height: 23px; color: var(--body-grey); }
  .step .read-more { display: block; margin-top: 3px; font-size: 13px; color: var(--red); text-decoration: none; }

  /* Plans */
  .plans { position: absolute; left: 0; top: 1112px; width: 1200px; height: 523px; background: var(--blue); }
  .plans .section-title { top: 30px; color: var(--white); }
  .plan-card { position: absolute; top: 91px; width: 372px; height: 297px; background: var(--white); border-radius: 9px; }
  .plan-name { position: absolute; left: 108px; top: 20px; width: 120px; text-align: center; font-family: var(--display); font-size: 20px; font-weight: 400; }
  .plan-price { position: absolute; left: 246px; top: 23px; font-size: 13px; }
  .plan-buy { position: absolute; left: 287px; top: 15px; width: 55px; height: 28px; border-radius: 4px; background: var(--blue);
    color: var(--white); font-family: var(--body); font-size: 12px; font-weight: 600; display: flex; align-items: center; justify-content: center; text-decoration: none; }
  .plan-shot { position: absolute; }
  .plan-shot.main { left: 16px; top: 62px; width: 203px; height: 200px; }
  .plan-shot.thumb { left: 237px; width: 105px; height: 97px; }
  .plan-shot.thumb.one { top: 54px; }
  .plan-shot.thumb.two { top: 165px; }
  .comfort .main { background: linear-gradient(160deg, #d9d6d2 0%, #c49a7c 45%, #1f6fd0 75%, #b58a6c 100%); }
  .comfort .thumb { background: linear-gradient(160deg, #1c1a1a 0%, #1d3a6c 60%, #151515 100%); }
  .style .main { background: linear-gradient(160deg, #d8d6d4 0%, #b98a6c 35%, #1a1a16 55%, #8ed62a 80%, #d8d6d4 100%); }
  .style .thumb { background: linear-gradient(160deg, #161616 0%, #2f4a18 60%, #151515 100%); }

  .perks { position: absolute; left: 100px; top: 416px; width: 1000px; height: 67px; background: var(--blue-deep);
    display: flex; align-items: center; color: var(--white); font-size: 15px; }
  .perk { position: absolute; display: flex; align-items: center; gap: 12px; white-space: nowrap; }

  /* FAQ */
  .faq { position: absolute; left: 0; top: 1635px; width: 1200px; height: 545px; background: var(--paper); }
  .faq .section-title { top: 41px; color: var(--ink); }
  .faq-item { position: absolute; width: 300px; margin-left: -150px; text-align: center; }
  .faq-item h3 { font-family: var(--display); font-weight: 400; font-size: 20px; color: var(--blue-text); }
  .faq-item p { margin-top: 4px; font-size: 14.5px; line-height: 23px; color: var(--body-grey); }

  /* Footer */
  .site-footer { position: absolute; left: 0; top: 2180px; width: 1200px; height: 128px; background: var(--footer); color: #dddddd; }
  .footer-links { position: absolute; left: 100px; top: 31px; font-size: 14.5px; line-height: 25px; }
  .payments { position: absolute; left: 622px; top: 28px; display: grid; grid-template-columns: 82px 82px; row-gap: 18px;
    font-family: var(--display); font-size: 14px; color: var(--white); }
  .social { position: absolute; left: 930px; top: 36px; display: flex; gap: 6px; }
  .social-item { width: 42px; display: flex; flex-direction: column; align-items: center; gap: 4px;
    font-family: var(--display); font-size: 9px; color: #dddddd; }
  .social-item span.dot { width: 32px; height: 32px; border-radius: 50%; background: #e9e9e9; }
  .age-mark { position: absolute; left: 1125px; top: 42px; font-size: 14px; }
</style>
</head>
<body>

<header class="site-header">
  <div class="brand"><span>Brickwell</span><span class="brand-dot"></span></div>
  <nav class="main-nav">
    <a href="#how">How It Works</a>
    <a href="#plans">Plans</a>
    <a href="#faq">FAQ</a>
    <a href="#about">About Us</a>
    <a class="signup" href="#plans">Sign Up Now</a>
  </nav>
</header>

<section class="hero">
  <svg class="hero-photo" viewBox="0 0 1200 494" role="img" aria-label="Model wearing blue briefs against a grey backdrop">
    <defs>
      <linearGradient id="heroShot" x1="0" y1="0" x2="1" y2="1">
        <stop offset="0" stop-color="#4a4a4a"/>
        <stop offset="0.45" stop-color="#b07a55"/>
        <stop offset="0.7" stop-color="#2b8fd0"/>
        <stop offset="1" stop-color="#8a5e42"/>
      </linearGradient>
    </defs>
    <polygon points="0,0 308,0 485,494 0,494" fill="url(#heroShot)"/>
  </svg>
  <div class="hero-copy">
    <h1 class="hero-title"><span class="dark">Automatate Your</span> Life</h1>
    <p class="hero-sub"><span class="dark">New</span> Underwear And Socks<br><span class="dark">Delivered To Your</span> Door</p>
    <p class="hero-when">When You Need IT</p>
  </div>
  <div class="slider-dots"><span class="active"></span><span></span><span></span></div>
</section>

<section class="how" id="how">
  <h2 class="section-title">How It Works</h2>
  <div class="step" style="left:280px">
    <div class="step-icon">
      <svg width="84" height="84" viewBox="0 0 84 84">
        <polygon points="42,6 78,22 42,38 6,22" fill="#fff"/>
        <polygon points="4,27 39,43 39,80 4,63" fill="#fff"/>
        <polygon points="80,27 45,43 45,80 80,63" fill="#fff"/>
      </svg>
    </div>
    <h3>Choose a Plan</h3>
    <p>Lorem ipsum dolor sit amet, consectetuer adipiscing elit. Aenean commodo ligula eget dolor. Aenean massa.</p>
    <a class="read-more" href="#plans">Read More +</a>
  </div>
  <div class="step" style="left:601px">
    <div class="step-icon">
      <svg width="84" height="70" viewBox="0 0 84 70">
        <polyline points="6,60 32,34 46,46 72,18" fill="none" stroke="#fff" stroke-width="9" stroke-linejoin="miter"/>
        <polygon points="56,8 82,6 80,32" fill="#fff"/>
      </svg>
    </div>
    <h3>Choose How Often</h3>
    <p>Lorem ipsum dolor sit amet, consectetuer adipiscing elit. Aenean commodo ligula eget dolor. Aenean massa.</p>
    <a class="read-more" href="#plans">Read More +</a>
  </div>
  <div class="step" style="left:917px">
    <div class="step-icon">
      <svg width="96" height="80" viewBox="0 0 96 80">
        <text x="48" y="30" text-anchor="middle" font-family="Open Sans, sans-serif" font-size="34" font-weight="600" fill="#fff">$</text>
        <circle cx="26" cy="44" r="10" fill="#fff"/>
        <path d="M4 78 Q4 58 26 58 Q48 58 48 78 Z" fill="#fff"/>
        <circle cx="70" cy="44" r="10" fill="#fff"/>
        <path d="M48 78 Q48 58 70 58 Q92 58 92 78 Z" fill="#fff"/>
      </svg>
    </div>
    <h3>Get your Pack</h3>
    <p>Lorem ipsum dolor sit amet, consectetuer adipiscing elit. Aenean commodo ligula eget dolor. Aenean massa.</p>
    <a class="read-more" href="#plans">Read More +</a>
  </div>
</section>

<section class="plans" id="plans">
  <h2 class="section-title">Plans</h2>
  <article class="plan-card comfort" style="left:195px">
    <h3 class="plan-name">Comfort</h3>
    <span class="plan-price">$30</span>
    <a class="plan-buy" href="#">Get It</a>
    <div class="plan-shot main" role="img" aria-label="Model wearing blue briefs"></div>
    <div class="plan-shot thumb one" role="img" aria-label="Navy briefs, front detail"></div>
    <div class="plan-shot thumb two" role="img" aria-label="Navy briefs, back detail"></div>
  </article>
  <article class="plan-card style" style="left:636px">
    <h3 class="plan-name">Style</h3>
    <span class="plan-price">$30</span>
    <a class="plan-buy" href="#">Get It</a>
    <div class="plan-shot main" role="img" aria-label="Model wearing lime and black briefs"></div>
    <div class="plan-shot thumb one" role="img" aria-label="Lime briefs, front detail"></div>
    <div class="plan-shot thumb two" role="img" aria-label="Lime briefs, back detail"></div>
  </article>
  <div class="perks">
    <div class="perk" style="left:52px"><svg width="22" height="18" viewBox="0 0 22 18"><polyline points="2,9 8,15 20,2" fill="none" stroke="#fff" stroke-width="3.5"/></svg>Free Shipping</div>
    <div class="perk" style="left:261px"><svg width="22" height="18" viewBox="0 0 22 18"><polyline points="2,9 8,15 20,2" fill="none" stroke="#fff" stroke-width="3.5"/></svg>Easy Returns</div>
    <div class="perk" style="left:473px"><svg width="22" height="18" viewBox="0 0 22 18"><polyline points="2,9 8,15 20,2" fill="none" stroke="#fff" stroke-width="3.5"/></svg>Cancel Whenever</div>
    <div class="perk" style="left:718px"><svg width="22" height="18" viewBox="0 0 22 18"><polyline points="2,9 8,15 20,2" fill="none" stroke="#fff" stroke-width="3.5"/></svg>Satisfaction Guaranteed</div>
  </div>
</section>

<section class="faq" id="faq">
  <h2 class="section-title">FAQ</h2>
  <div class="faq-item" style="left:282px;top:110px"><h3>What is Brickwell?</h3><p>Lorem ipsum dolor sit amet, consectetuer adipiscing elit. Aenean commodo ligula eget dolor. Aenean massa.</p></div>
  <div class="faq-item" style="left:598px;top:110px"><h3>What is your statsifaction</h3><p>Lorem ipsum dolor sit amet, consectetuer adipiscing elit. Aenean commodo ligula eget dolor. Aenean massa.</p></div>
  <div class="faq-item" style="left:918px;top:110px"><h3>Shipping Cart</h3><p>Lorem ipsum dolor sit amet, consectetuer adipiscing elit. Aenean commodo ligula eget dolor. Aenean massa.</p></div>
  <div class="faq-item" style="left:282px;top:252px"><h3>What is Brickwell?</h3><p>Lorem ipsum dolor sit amet, consectetuer adipiscing elit. Aenean commodo ligula eget dolor. Aenean massa.</p></div>
  <div class="faq-item" style="left:598px;top:252px"><h3>What is your statsifaction</h3><p>Lorem ipsum dolor sit amet, consectetuer adipiscing elit. Aenean commodo ligula eget dolor. Aenean massa.</p></div>
  <div class="faq-item" style="left:918px;top:252px"><h3>Shipping Cart</h3><p>Lorem ipsum dolor sit amet, consectetuer adipiscing elit. Aenean commodo ligula eget dolor. Aenean massa.</p></div>
  <div class="faq-item" style="left:282px;top:384px"><h3>What is Brickwell?</h3><p>Lorem ipsum dolor sit amet, consectetuer adipiscing elit. Aenean commodo ligula eget dolor. Aenean massa.</p></div>
  <div class="faq-item" style="left:598px;top:384px"><h3>What is your statsifaction</h3><p>Lorem ipsum dolor sit amet, consectetuer adipiscing elit. Aenean commodo ligula eget dolor. Aenean massa.</p></div>
  <div class="faq-item" style="left:918px;top:384px"><h3>Shipping Cart</h3><p>Lorem ipsum dolor sit amet, consectetuer adipiscing elit. Aenean commodo ligula eget dolor. Aenean massa.</p></div>
</section>

<footer class="site-footer">
  <div class="footer-links">
    <p>Shipping / Returns / Payment / Terms / Privacy</p>
    <p>© 2014 Company Name &nbsp;All right reserved &nbsp;Term of Use</p>
  </div>
  <div class="payments">
    <span>Norvecard</span><span>Ambrelo</span>
    <span>Mistrelle</span><span>Quoppa</span>
  </div>
  <div class="social">
    <div class="social-item"><span class="dot"></span>Kindrel</div>
    <div class="social-item"><span class="dot"></span>Pictova</div>
    <div class="social-item"><span class="dot"></span>Chatwick</div>
    <div class="social-item"><span class="dot"></span>Reelden</div>
  </div>
  <span class="age-mark">X18</span>
</footer>

</body>
</html>
```